Redesign our Product Box!

We have a product box for our pet supplement we are looking to redesign. Please use the photoshop file of the current design for the logo/info/dieline and the concept picture of a bag we would like to see included in the box design.

Ideally the background will be the green with white text, but we really want it to be fun and appealing to pet owners so do not be scared to show your vision.

```html
<!DOCTYPE html>
<html lang="en">
<head>
<meta charset="utf-8">
<title>MarinePaw Product Box Dieline</title>
<link href="https://fonts.googleapis.com/css2?family=Montserrat:wght@400;500;600;700;800&display=swap" rel="stylesheet">
<style>
  :root {
    --bg: #d1d3d4;
    --green: #00a651;
    --white: #ffffff;
    --mark: #1fb866;
    --ink: #1a1a1a;
  }
  * { margin: 0; padding: 0; box-sizing: border-box; }
  html, body { width: 1200px; height: 1000px; overflow: hidden; background: var(--bg); }
  body { font-family: "Montserrat", sans-serif; color: var(--white); }
  .canvas { position: relative; width: 1200px; height: 1000px; }
  .dieline { position: absolute; left: 0; top: 0; }
  .dieline path, .dieline rect { fill: var(--green); }
  .abs { position: absolute; }
  .c { text-align: center; }

  .brand-top { left: 232px; top: 188px; font-size: 27px; font-weight: 800; letter-spacing: -0.5px; }
  .brand-mark { left: 196px; top: 322px; width: 152px; height: 134px; background: var(--mark); border-radius: 8px; }
  .front-title { left: 231px; top: 478px; font-size: 18.5px; font-weight: 700; line-height: 1.27; }
  .front-sub { left: 231px; top: 585px; font-size: 13.5px; font-weight: 500; line-height: 1.28; }
  .front-weight { left: 236px; top: 662px; font-size: 14px; font-weight: 500; }
  .brand-side { left: 418px; top: 500px; transform: translate(-50%, -50%) rotate(-90deg); font-size: 50px; font-weight: 800; white-space: nowrap; letter-spacing: -1px; }

  .directions { left: 462px; top: 311px; width: 168px; font-size: 10px; font-weight: 700; line-height: 1.28; }
  .rule { left: 477px; top: 400px; width: 130px; height: 3px; background: var(--white); }
  .treasure { left: 462px; top: 418px; width: 168px; font-size: 13px; line-height: 1.35; }
  .treasure h2 { font-size: 13px; font-weight: 700; margin-bottom: 6px; line-height: 1.3; }
  .treasure p { font-size: 11.5px; font-weight: 500; margin-bottom: 10px; line-height: 1.33; }

  .print-side { left: 706px; top: 180px; font-size: 27px; color: var(--green); line-height: 1.2; }

  .facts { left: 640px; top: 314px; width: 211px; height: 156px; background: var(--white); color: var(--green); padding: 5px; }
  .facts-box { border: 1.5px solid var(--green); }
  .facts-box h3 { font-size: 18px; font-weight: 700; padding: 2px 4px; border-bottom: 2.5px solid var(--green); text-align: center; }
  .facts-row { font-size: 6.5px; padding: 2px 4px; border-bottom: 1px solid var(--green); display: flex; justify-content: space-between; align-items: flex-end; line-height: 1.3; }
  .facts-row.item { padding: 6px 4px; }
  .facts-row.note { border-bottom: none; padding: 6px 4px 8px; }
  .facts-legal { font-size: 5px; margin-top: 5px; line-height: 1.25; }
  .facts-store { font-size: 5px; margin-top: 4px; }

  .dist { left: 646px; top: 508px; width: 210px; font-size: 11px; line-height: 1.4; }
  .dist strong { font-weight: 600; }
  .warnings { left: 646px; top: 588px; width: 210px; font-size: 6.5px; line-height: 1.32; }
  .care { left: 630px; top: 655px; width: 228px; font-size: 11px; font-weight: 600; line-height: 1.45; }

  .story { left: 862px; top: 311px; width: 170px; font-size: 11.5px; font-weight: 500; line-height: 1.24; }
  .story p { margin-bottom: 13px; }

  .lot { left: 655px; top: 850px; transform: rotate(180deg); font-size: 11px; color: var(--ink); white-space: nowrap; }
</style>
</head>
<body>
<main class="canvas">
  <svg class="dieline" width="1200" height="1000" viewBox="0 0 1200 1000" aria-hidden="true">
    <path d="M228 172 V118 Q228 48 300 48 H378 Q450 48 450 118 V172 Z"/>
    <rect x="225" y="172" width="228" height="530"/>
    <path d="M170 302 L225 297 V702 H170 Z"/>
    <path d="M453 172 H612 V268 L630 282 V297 H858 V715 H630 L453 715 Z"/>
    <path d="M878 172 H1033 V720 H858 V297 L878 280 Z"/>
    <path d="M462 715 H612 V828 H472 L462 760 Z"/>
    <path d="M630 715 H858 V885 H855 V892 Q855 955 775 955 H713 Q633 955 633 892 V885 H630 Z"/>
    <path d="M858 720 H1018 V760 L1008 828 H858 Z"/>
  </svg>

  <div class="abs brand-top">MarinePaw</div>
  <div class="abs brand-mark" role="img" aria-label="Brand symbol area"></div>
  <div class="abs front-title">100% Pure<br>Marine<br>Phytoplankton<br>Powder</div>
  <div class="abs front-sub">Foundational Nutrition<br>&amp; Super-Antioxidant<br>For Dogs &amp; Cats</div>
  <div class="abs front-weight">15g</div>
  <div class="abs brand-side">MarinePaw</div>

  <div class="abs directions c">Directions:<br>For dogs &amp; cats 1/16 tsp<br>once per day.<br>Administer orally.<br>To be mixed into food.<br>1/16tsp = 1/2 the<br>included scoop.</div>
  <div class="abs rule"></div>
  <section class="abs treasure c">
    <h2>Unlock Nature’s<br>Nutrient Treasure:</h2>
    <p>Phytoplankton is the foundation of life, It is the first plant in the entire food chain.</p>
    <p>Phytoplankton is a microscopic powerhouse. Your pet’s body absorbs billions of phytoplankton with every serving.</p>
    <p>Packed with the building blocks of life, phytoplankton addresses multiple aspects of your pet’s health in one simple supplement.</p>
  </section>

  <div class="abs print-side">PRINT<br>SIDE</div>

  <section class="abs facts">
    <div class="facts-box">
      <h3>Supplement Facts</h3>
      <div class="facts-row"><span>Serving Size: 1 Scoop/Day<br>Servings per Container: 30</span><span>Amount per Serving &nbsp;%DV</span></div>
      <div class="facts-row item"><span>Microalgae Nannochloropsis Gaditana</span><span>500mg &nbsp;‡</span></div>
      <div class="facts-row note"><span>‡ Daily value not established.</span></div>
    </div>
    <div class="facts-legal">These statements have not been evaluated by the Food and Drug Administration. This product is not intended to diagnose, treat, cure, or prevent any disease.</div>
    <div class="facts-store">Store in a cool dry place.</div>
  </section>

  <div class="abs dist"><strong>Distributed By:</strong><br>Bluewave Pet Nutrition Inc.<br>42 Harbour Lane,<br>Seabrook, Nova Scotia<br>Canada B0A 1Z0</div>
  <div class="abs warnings">Warnings: Check with a qualified healthcare professional before using this product if you are pregnant, breastfeeding, or taking blood thinners. You should call your doctor for medical advice about serious adverse events. To report a serious adverse event or obtain product information contact:</div>
  <div class="abs care c">Customer Care: 1 800 555 0142<br>bluewavepets.com</div>

  <section class="abs story c">
    <p>Our premium phytoplankton powder is an extraordinary supplement. It infuses your pet’s body with pure, plant-based nutrients and potent antioxidants.</p>
    <p>Phytoplankton goes beyond ordinary supplements; it’s a path to optimal health. In just a few weeks, your pet will experience a feeling of calm and strength, the kind of wellness our customers often say they’ve been seeking.</p>
    <p>Join those who have discovered the transformative power of phytoplankton. See the difference for yourself and understand why it’s not just a supplement, but a revolution in pet health and vitality.</p>
  </section>

  <div class="abs lot">Exp: 22025/03/Lot No.:1 2222</div>
</main>
</body>
</html>
```